U.S. based testing, inspection, and certification (TIC) company needs a new PowerPoint template.

We need a new PowerPoint template (deck, slide deck) for our U.S. based company with international capabilities for performing numerous testing, inspection, and certification (TIC) services. Our primary services include calibration, chemical analysis, consulting engineering, environmental simulation, forensic engineering, materials testing, mechanical testing, and nondestructive testing. Industries we serve are aerospace/aviation, automotive, chemical, commercial properties, construction, consumer products, defense, energy storage, healthcare, insurance/legal, life science, manufacturing, oil & gas, power generation, pulp & paper, and telecommunications. https://qorvenlab.com/

Guideline hex colors: #29aae2, #0b1f3b, #fb6805 (use orange more subtly)

The final design should communicate:
1. Trust, Integrity, and Independence
2. Technical Expertise and Accuracy
3. Efficiency and Speed
4. Value-Added Partnership

Our current branding reflects a variety of styles, several of which have been included as attachments for reference in this project. While these examples showcase the direction we have taken in the past, we are not limited to them and remain open to exploring fresh, innovative design that is simple, clean, and with plenty of space to add content for each slide. We welcome creative concepts that build on or reimagine our existing identity to better align with our evolving vision.

```html
<!DOCTYPE html>
<html lang="en">
<head>
<meta charset="utf-8">
<title>Qorven Laboratories – Presentation Template</title>
<link href="https://fonts.googleapis.com/css2?family=Inter:wght@400;500;700;800;900&family=Plus+Jakarta+Sans:wght@400;500;600;700&display=swap" rel="stylesheet">
<style>
:root{
  --page:#1c1c1c;
  --navy-top:#0d4b85;
  --navy-bottom:#07203f;
  --orange:#d9490a;
  --orange-soft:#e0541a;
  --white:#ffffff;
  --text-soft:#d8e4f0;
  --rule:rgba(150,190,230,.45);
}
*{margin:0;padding:0;box-sizing:border-box}
html,body{width:1029px;height:1200px;overflow:hidden;background:var(--page)}
body{position:relative;font-family:"Plus Jakarta Sans",Arial,sans-serif;color:var(--white)}
.slide{position:absolute;width:457px;height:258px;overflow:hidden;
  background:linear-gradient(180deg,var(--navy-top) 0%,#0b3a6c 45%,var(--navy-bottom) 100%)}
.col-left{left:39px}.col-right{left:534px}
.row-1{top:41px}.row-2{top:328px}.row-3{top:614px}.row-4{top:901px}
.slide-title{position:absolute;left:24px;top:7px;font-family:Inter,Arial,sans-serif;font-weight:500;font-size:15px;letter-spacing:.2px;text-transform:uppercase}
.title-rule{position:absolute;left:0;top:32px;width:290px;height:1px;background:var(--rule)}
.footer{position:absolute;left:0;bottom:0;width:100%;height:19px;background:var(--orange);
  font-size:5.2px;display:flex;align-items:center;padding:0 24px}
.footer .sep{margin:0 9px}
.footer .copy{margin-left:auto}
/* cover */
.cover{background:#080c14}
.cover-photo{position:absolute;inset:0;background:radial-gradient(ellipse at 45% 25%,#5f7d99 0%,#2a3f58 30%,#0e1622 65%,#05070b 100%)}
.brand{position:absolute;font-family:"Plus Jakarta Sans",Arial,sans-serif;font-weight:700;color:var(--white);white-space:nowrap}
.cover .brand{right:32px;top:30px;font-size:10px}
.cover-headline{position:absolute;left:24px;top:184px;font-family:Inter,Arial,sans-serif;font-weight:800;font-size:22.5px;line-height:28px;text-transform:uppercase}
/* unique */
.quote-mark{position:absolute;left:37px;top:66px;width:80px;height:58px}
.unique-copy{position:absolute;left:160px;top:60px;width:261px;font-size:6.9px;line-height:13.6px;color:var(--text-soft);text-align:justify}
.unique-copy p+p{margin-top:13.6px}
.accent-heading{position:absolute;left:160px;top:168px;width:270px;font-family:Inter,Arial,sans-serif;font-weight:800;font-size:12.5px;line-height:19px;color:var(--orange-soft);text-transform:uppercase}
/* contents */
.contents-photo{position:absolute;left:35px;top:61px;width:205px;height:148px;background:linear-gradient(160deg,#3c5a2e 0%,#8d9a86 45%,#c9c7bd 55%,#2f4727 100%)}
.contents-list{position:absolute;left:289px;top:68px;list-style:none;font-size:6.7px}
.contents-list li{height:20.3px;display:flex}
.contents-list .num{width:17px}
/* obstacles */
.service{position:absolute;width:150px}
.service h3{font-family:Inter,Arial,sans-serif;font-weight:500;font-size:9px;margin-bottom:3px}
.service p{font-size:5.6px;line-height:9.6px;color:var(--text-soft)}
.service.left{left:36px;text-align:right}
.service.left h3{color:var(--orange-soft)}
.service.right{left:290px;text-align:left}
.arrow-art{position:absolute;left:196px;top:52px;width:84px;height:172px;
  background:linear-gradient(180deg,#d9490a 0%,#e9e4df 30%,#d9490a 55%,#e9e4df 85%,#d9d4cf 100%);opacity:.9}
/* provide */
.intro{position:absolute;left:60px;top:45px;width:337px;text-align:center;font-size:6.6px;line-height:13px;color:var(--text-soft)}
.subhead{position:absolute;left:0;width:100%;top:100px;text-align:center;font-size:7px}
.feature{position:absolute;top:126px;width:118px;text-align:center}
.feature .badge{width:42px;height:42px;border-radius:50%;background:var(--orange);margin:0 auto 9px;display:flex;align-items:center;justify-content:center}
.feature h4{font-family:Inter,Arial,sans-serif;font-weight:700;font-size:6px;color:var(--orange-soft);margin-bottom:2px}
.feature p{font-size:5.8px;line-height:10.7px;color:var(--text-soft)}
/* needs */
.needs-list{position:absolute;left:123px;top:48px;list-style:none}
.needs-list li{width:212px;height:22px;margin-bottom:12px;display:flex;align-items:center;padding-left:11px;font-size:7.5px;
  background:linear-gradient(90deg,rgba(80,130,180,.28) 0%,rgba(80,130,180,.12) 70%,rgba(80,130,180,0) 100%)}
.needs-list .num{width:21px}
/* divider */
.divider-bg{position:absolute;inset:0;background:radial-gradient(ellipse at 50% 30%,#1b5a95 0%,#0b3563 55%,#061c36 100%)}
.divider-frame{position:absolute;left:35px;top:31px;width:387px;height:195px;border:1.5px solid var(--orange)}
.divider .brand{left:0;width:100%;top:56px;text-align:center;font-size:15px}
.divider-band{position:absolute;left:0;top:101px;width:100%;height:98px;background:var(--orange);text-align:center}
.divider-band h2{font-family:Inter,Arial,sans-serif;font-weight:800;font-size:17px;margin-top:23px}
.divider-band p{font-size:8.5px;line-height:14px;margin-top:5px}
/* closing */
.chat-badge{position:absolute;left:202px;top:39px;width:52px;height:52px;border-radius:50%;background:var(--orange);display:flex;align-items:center;justify-content:center}
.closing-text{position:absolute;left:0;width:100%;text-align:center}
.thanks{top:117px;font-size:7.6px}
.big-line{top:128px;font-family:Inter,Arial,sans-serif;font-weight:900;font-size:25px;letter-spacing:.3px}
.mid-line{top:158px;font-family:Inter,Arial,sans-serif;font-weight:800;font-size:13.5px}
.closing-copy{top:182px;left:70px;width:317px;font-size:7.5px;line-height:13.5px;color:var(--text-soft)}
</style>
</head>
<body>

<!-- Cover -->
<section class="slide cover col-left row-1">
  <div class="cover-photo" role="img" aria-label="Close-up photograph of turbine engine fan blades in cool blue light"></div>
  <div class="brand">Qorven Laboratories</div>
  <h1 class="cover-headline">We take you from<br>confidence to certainty</h1>
</section>

<!-- What makes us unique -->
<section class="slide col-right row-1">
  <h2 class="slide-title">What makes us unique</h2>
  <div class="title-rule"></div>
  <svg class="quote-mark" viewBox="0 0 80 58" aria-hidden="true">
    <path d="M0 0H34V26L22 58H8L16 30H0Z" fill="#d9490a"/>
    <path d="M46 0H80V26L68 58H54L62 30H46Z" fill="#d9490a"/>
  </svg>
  <div class="unique-copy">
    <p>Experts in metallurgy, materials testing, chemical analysis, non-destructive testing, calibrations, fire investigation and forensics.</p>
    <p>Whether you need to protect it, prove it, or improve it, Qorven is ready to partner with you in quality, safety, and reliability. With deep experience in testing, engineering, inspection, and calibration for a wide range of industries, our experts offer insight and guidance for those seeking certainty.</p>
  </div>
  <div class="accent-heading">Your partner in quality, safety, &amp; reliability</div>
  <div class="footer"><span>Call Us: +1 888-555-0148</span><span class="sep">|</span><span>Email Us: customerservice@qorvenlab.com</span><span class="copy">(C) Copyright 2026 Qorven Laboratories &nbsp;|&nbsp; All Rights Reserved</span></div>
</section>

<!-- Table of contents -->
<section class="slide col-left row-2">
  <h2 class="slide-title">Table of contents</h2>
  <div class="title-rule"></div>
  <div class="contents-photo" role="img" aria-label="Aerial photograph of the company laboratory building surrounded by trees and a parking lot"></div>
  <ol class="contents-list">
    <li><span class="num">01)</span>Introduction</li>
    <li><span class="num">02)</span>Table of Contents (Agenda)</li>
    <li><span class="num">03)</span>What We Provice</li>
    <li><span class="num">04)</span>What Makes Us Unique</li>
    <li><span class="num">05)</span>Your Partner in Overcoming Obstacles</li>
    <li><span class="num">06)</span>How Qorven Meets Customer Needs</li>
    <li><span class="num">07)</span>How it works</li>
  </ol>
  <div class="footer"><span>Call Us: +1 888-555-0148</span><span class="sep">|</span><span>Email Us: customerservice@qorvenlab.com</span><span class="copy">(C) Copyright 2026 Qorven Laboratories &nbsp;|&nbsp; All Rights Reserved</span></div>
</section>

<!-- Overcoming obstacles -->
<section class="slide col-right row-2">
  <h2 class="slide-title">Your partner in overcoming obstacles</h2>
  <div class="title-rule"></div>
  <div class="service left" style="top:63px">
    <h3>TESTING</h3>
    <p>Ensure your products meet the highest standards of quality and safety with Qorven's comprehensive testing services.</p>
  </div>
  <div class="service left" style="top:140px">
    <h3>CALIBRATION</h3>
    <p>Maintain precision and accuracy across all your instruments with Qorven's calibration services. Our highly trained specialists ensure your equipment</p>
  </div>
  <div class="service right" style="top:101px">
    <h3>INSPECTION</h3>
    <p>Gain confidence in the integrity of your assets with Qorven's meticulous inspection services. Our experienced inspectors use advanced techniques</p>
  </div>
  <div class="service right" style="top:178px">
    <h3>FORENSIC</h3>
    <p>Uncover the root causes of failures and prevent future issues with Qorven's forensic services. Our skilled investigators employ rigorous analysis</p>
  </div>
  <div class="arrow-art" role="img" aria-label="Illustration of interlocking orange and white arrows linking the four services"></div>
  <div class="footer"><span>Call Us: +1 888-555-0148</span><span class="sep">|</span><span>Email Us: customerservice@qorvenlab.com</span><span class="copy">(C) Copyright 2026 Qorven Laboratories &nbsp;|&nbsp; All Rights Reserved</span></div>
</section>

<!-- What we provide -->
<section class="slide col-left row-3">
  <h2 class="slide-title">What we provide</h2>
  <div class="title-rule"></div>
  <p class="intro">Every industry has its hurdles, and at Qorven, we're here to help you navigate them. Our broad spectrum of specialized services is customized to meet each client's unique challenges head-on. Experience the Qorven advantage where innovative, tailored solutions and dedicated support propel you towards your goals.</p>
  <p class="subhead">Your Partner in Overcoming Obstacles</p>
  <div class="feature" style="left:52px">
    <div class="badge"><svg width="18" height="18" viewBox="0 0 24 24" aria-hidden="true"><path d="M12 1l3 2.6 3.9-.3.8 3.8 3.3 2.1-1.6 3.6 1.6 3.6-3.3 2.1-.8 3.8-3.9-.3L12 23l-3-2.6-3.9.3-.8-3.8L1 14.8 2.6 11.2 1 7.6l3.3-2.1.8-3.8 3.9.3z" fill="#fff"/><path d="M7.5 12l3 3 6-6" stroke="#d9490a" stroke-width="2.4" fill="none" stroke-linecap="round"/></svg></div>
    <h4>INSPECTION</h4>
    <p>Our thorough inspection services use cutting-edge techniques to guarantee the highest levels of safety</p>
  </div>
  <div class="feature" style="left:170px">
    <div class="badge"><svg width="18" height="18" viewBox="0 0 24 24" aria-hidden="true"><path d="M12 1l3 2.6 3.9-.3.8 3.8 3.3 2.1-1.6 3.6 1.6 3.6-3.3 2.1-.8 3.8-3.9-.3L12 23l-3-2.6-3.9.3-.8-3.8L1 14.8 2.6 11.2 1 7.6l3.3-2.1.8-3.8 3.9.3z" fill="#fff"/><path d="M7.5 12l3 3 6-6" stroke="#d9490a" stroke-width="2.4" fill="none" stroke-linecap="round"/></svg></div>
    <h4>TESTING &amp; ANALYSIS</h4>
    <p>From materials testing to environmental simulations, our expert team is dedicated</p>
  </div>
  <div class="feature" style="left:288px">
    <div class="badge"><svg width="18" height="18" viewBox="0 0 24 24" aria-hidden="true"><path d="M12 1l3 2.6 3.9-.3.8 3.8 3.3 2.1-1.6 3.6 1.6 3.6-3.3 2.1-.8 3.8-3.9-.3L12 23l-3-2.6-3.9.3-.8-3.8L1 14.8 2.6 11.2 1 7.6l3.3-2.1.8-3.8 3.9.3z" fill="#fff"/><path d="M7.5 12l3 3 6-6" stroke="#d9490a" stroke-width="2.4" fill="none" stroke-linecap="round"/></svg></div>
    <h4>TRAINING</h4>
    <p>Explore our training courses below and take the next step toward professional development.</p>
  </div>
  <div class="footer"><span>Call Us: +1 888-555-0148</span><span class="sep">|</span><span>Email Us: customerservice@qorvenlab.com</span><span class="copy">(C) Copyright 2026 Qorven Laboratories &nbsp;|&nbsp; All Rights Reserved</span></div>
</section>

<!-- Customer needs -->
<section class="slide col-right row-3">
  <h2 class="slide-title">How Qorven meets customer needs</h2>
  <div class="title-rule"></div>
  <ol class="needs-list">
    <li><span class="num">01)</span>Compliance with Standards</li>
    <li><span class="num">02)</span>Timely Professional Services</li>
    <li><span class="num">03)</span>Clear &amp; Accurate Data</li>
    <li><span class="num">04)</span>Qualified Team</li>
    <li><span class="num">05)</span>Stay ahead of the curve with Qorven insights</li>
  </ol>
  <div class="footer"><span>Call Us: +1 888-555-0148</span><span class="sep">|</span><span>Email Us: customerservice@qorvenlab.com</span><span class="copy">(C) Copyright 2026 Qorven Laboratories &nbsp;|&nbsp; All Rights Reserved</span></div>
</section>

<!-- Section divider -->
<section class="slide divider col-left row-4">
  <div class="divider-bg" role="img" aria-label="Blue-tinted aerial city view with glowing network lines"></div>
  <div class="divider-frame"></div>
  <div class="brand">Qorven Laboratories</div>
  <div class="divider-band">
    <h2>SECTION DEVIDER</h2>
    <p>Sed ut perspiciatis unde omnis iste natus error sit voluptatem<br>accusantium doloremque laudantium,</p>
  </div>
</section>

<!-- Closing -->
<section class="slide col-right row-4">
  <div class="chat-badge">
    <svg width="26" height="22" viewBox="0 0 26 22" aria-hidden="true">
      <ellipse cx="10" cy="8" rx="9.5" ry="7" fill="#fff"/>
      <path d="M4 13l-2 5 6-3z" fill="#fff"/>
      <ellipse cx="17" cy="13" rx="8" ry="6" fill="#fff" stroke="#d9490a" stroke-width="1.5"/>
      <path d="M21 17l3 4-6-2z" fill="#fff"/>
    </svg>
  </div>
  <p class="closing-text thanks">THANK YOU FOR YOUR TIME AND ATTENTION.</p>
  <p class="closing-text big-line">INDEPENDENT EXPERTISE.</p>
  <p class="closing-text mid-line">TRUSTED RESULTS. PROVEN SOLUTIONS.</p>
  <p class="closing-text closing-copy">Whether you need testing, inspection, certification, engineering consulting, or analytical services, Qorven is committed to delivering trusted expertise, accurate results, and responsive support.</p>
</section>

</body>
</html>
```